Torvel, Inc. new buisness cards - brand guide included

We need new business cards. SLEAK SIMPLE FINANCE. They must include a place for NAME, TITLE, CELL, OFFICE PHONE, EMAIL. they also must include our services across the bottom. AIR, OCEAN, FTL, LTL, EXPRESS. for reference this will be being handed to some of the most prestigious shipping companies in a america.

Target Market(s)

Finance and corporate

Contact Information for Business Card

We need new business cards. SLEAK SIMPLE FINANCE. They must include a place for NAME, TITLE, CELL, OFFICE PHONE, EMAIL. they also must include our services across the bottom. AIR, OCEAN, FTL, LTL, EXPRESS.

Requirements
Must have
• We need new business cards. SLEAK SIMPLE FINANCE. They must include a place for NAME, TITLE, CELL, OFFICE PHONE, EMAIL. they also must include our services across the bottom. AIR, OCEAN, FTL, LTL, EXPRESS.
Nice to have
• USE THE COLORS AND LOGO IN THE BRAND GUIDE :)

```html
<!DOCTYPE html>
<html lang="en">
<head>
<meta charset="utf-8">
<title>Torvel, Inc. — Business Card</title>
<link rel="stylesheet" href="https://fonts.googleapis.com/css2?family=EB+Garamond:wght@400;600;700&display=swap">
<style>
  :root {
    --backdrop: #3a3a3c;
    --sand: #c8b99a;
    --ink: #231f20;
    --paper: #ffffff;
    --text: #2b2b2b;
    --band: #1c1c1c;
  }
  * { margin: 0; padding: 0; box-sizing: border-box; }
  html, body { width: 1200px; height: 758px; overflow: hidden; }
  body {
    background: var(--backdrop);
    font-family: "EB Garamond", "Times New Roman", serif;
    display: flex;
    align-items: center;
    justify-content: center;
    gap: 40px;
  }
  .card {
    position: relative;
    width: 540px;
    height: 310px;
    border-radius: 22px;
    overflow: hidden;
  }
  .card-front {
    background: var(--sand);
    display: flex;
    align-items: center;
    justify-content: center;
  }
  .brand-name {
    font-weight: 400;
    letter-spacing: 0.12em;
    text-transform: uppercase;
    line-height: 1;
  }
  .card-front .brand-name { font-size: 74px; color: var(--ink); }

  .card-back { background: var(--paper); }
  .wave { position: absolute; inset: 0; width: 100%; height: 100%; }
  .back-brand {
    position: absolute;
    left: 24px;
    top: 100px;
    width: 210px;
    text-align: center;
  }
  .back-brand .brand-name { font-size: 44px; color: var(--sand); }
  .divider {
    position: absolute;
    left: 252px;
    top: 34px;
    width: 1.5px;
    height: 150px;
    background: var(--sand);
  }
  .contact {
    position: absolute;
    left: 272px;
    top: 26px;
    color: var(--text);
  }
  .contact-name {
    font-size: 21px;
    font-weight: 700;
    letter-spacing: 0.03em;
    text-transform: uppercase;
    line-height: 1.1;
  }
  .contact-title { font-size: 15px; margin-bottom: 8px; }
  .contact-address { font-size: 14px; line-height: 1.2; margin-bottom: 6px; }
  .contact-list { list-style: none; font-size: 13.5px; line-height: 1.35; }
  .contact-list li { display: flex; align-items: center; gap: 7px; }
  .contact-list svg { width: 11px; height: 11px; fill: var(--sand); flex: none; }
  .services {
    position: absolute;
    right: 26px;
    bottom: 18px;
    color: var(--sand);
    font-size: 14px;
    letter-spacing: 0.06em;
  }
</style>
</head>
<body>
  <section class="card card-front" aria-label="Card front">
    <span class="brand-name">Torvel</span>
  </section>

  <section class="card card-back" aria-label="Card back">
    <svg class="wave" viewBox="0 0 540 310" preserveAspectRatio="none" aria-hidden="true">
      <path d="M0,262 C160,276 330,230 540,118 L540,310 L0,310 Z" fill="#c8b99a"/>
      <path d="M0,270 C160,284 330,238 540,128 L540,310 L0,310 Z" fill="#ffffff"/>
      <path d="M0,278 C160,292 330,248 540,140 L540,310 L0,310 Z" fill="#1c1c1c"/>
    </svg>

    <div class="back-brand"><span class="brand-name">Torvel</span></div>
    <div class="divider"></div>

    <div class="contact">
      <p class="contact-name">Daniel Harwick</p>
      <p class="contact-title">Founder &amp; CEO</p>
      <p class="contact-address">4120 Alder Creek RD<br>Dover, DE 19901</p>
      <ul class="contact-list">
        <li><svg viewBox="0 0 24 24"><path d="M6.6 10.8a15 15 0 0 0 6.6 6.6l2.2-2.2a1 1 0 0 1 1-.25 11.4 11.4 0 0 0 3.6.57 1 1 0 0 1 1 1V20a1 1 0 0 1-1 1A17 17 0 0 1 3 4a1 1 0 0 1 1-1h3.5a1 1 0 0 1 1 1c0 1.25.2 2.45.57 3.57a1 1 0 0 1-.25 1z"/></svg>555-010-2481</li>
        <li><svg viewBox="0 0 24 24"><path d="M7 1h10a2 2 0 0 1 2 2v18a2 2 0 0 1-2 2H7a2 2 0 0 1-2-2V3a2 2 0 0 1 2-2zm0 3v15h10V4z"/></svg>555-010-7734</li>
        <li><svg viewBox="0 0 24 24"><path d="M2 5h20v14H2zm2 2v.5l8 5 8-5V7z"/></svg>accounting@torvelinc.com</li>
        <li><svg viewBox="0 0 24 24"><circle cx="12" cy="12" r="10"/></svg>www.torvelinc.com</li>
      </ul>
    </div>

    <p class="services">• AIR • OCEAN • FTL • LTL • EXPRESS</p>
  </section>
</body>
</html>
```